Our website is qadtechhelp.net
We travel on site to help people/businesses with their computer issues.
This postcard is going to existing customers... just trying to touch them again.
QAD Tech provides a full line of residential and commercial computer support.

I've attached some stuff that I have done.

Industry/Entity Type

Residential

```html
<!DOCTYPE html>
<html lang="en">
<head>
<meta charset="utf-8">
<title>QAD Tech – Postcard</title>
<link rel="stylesheet" href="https://fonts.googleapis.com/css2?family=PT+Sans+Narrow:wght@700&family=Source+Sans+3:wght@400;600&display=swap">
<style>
  :root {
    --lime: #a8cf04;
    --lime-panel: #c1dd4d;
    --lime-pale: #d4e88b;
    --blue: #2b3df2;
    --white: #ffffff;
  }
  html, body {
    margin: 0;
    padding: 0;
    width: 1200px;
    height: 929px;
    overflow: hidden;
    background: var(--lime);
  }
  .postcard {
    position: relative;
    width: 1200px;
    height: 929px;
    background: var(--lime);
    font-family: "Source Sans 3", "Myriad Pro", sans-serif;
    color: var(--blue);
  }
  .brand {
    position: absolute;
    left: 0;
    top: 21px;
    width: 342px;
    height: 128px;
    background: var(--lime-pale);
    display: flex;
    align-items: center;
    justify-content: center;
  }
  .brand-name {
    font-family: "Source Sans 3", "Myriad Pro", sans-serif;
    font-weight: 600;
    font-size: 52px;
    color: var(--blue);
    letter-spacing: 0.5px;
  }
  .headline {
    position: absolute;
    left: 77px;
    top: 254px;
    margin: 0;
    font-family: "PT Sans Narrow", "Myriad Pro Condensed", sans-serif;
    font-weight: 700;
    font-size: 43px;
    line-height: 1;
    color: var(--blue);
    letter-spacing: -0.3px;
  }
  .plan {
    position: absolute;
    left: 34px;
    top: 347px;
    width: 396px;
    height: 335px;
    border-radius: 30px;
    background: var(--lime-panel);
  }
  .plan-list {
    list-style: none;
    margin: 0;
    padding: 0;
    position: absolute;
    left: 45px;
    top: 36px;
  }
  .plan-item {
    display: flex;
    align-items: center;
    height: 53px;
    font-size: 30px;
    color: var(--blue);
  }
  .tick {
    width: 24px;
    height: 24px;
    margin-right: 25px;
    flex: none;
  }
  .plan-price {
    position: absolute;
    left: 41px;
    top: 252px;
    margin: 0;
    font-size: 32px;
    color: var(--white);
  }
  .contact {
    position: absolute;
    left: 28px;
    top: 722px;
    display: flex;
    align-items: baseline;
    font-family: "PT Sans Narrow", "Myriad Pro Condensed", sans-serif;
    font-weight: 700;
    color: var(--blue);
  }
  .contact-phone { font-size: 45px; }
  .contact-web { font-size: 26px; margin-left: 56px; }
</style>
</head>
<body>
  <main class="postcard">
    <div class="brand"><span class="brand-name">QAD Tech</span></div>

    <h1 class="headline">We Also Make Housecalls!</h1>

    <section class="plan">
      <ul class="plan-list">
        <li class="plan-item"><svg class="tick" viewBox="0 0 24 24"><rect x="1.5" y="3.5" width="19" height="19" fill="none" stroke="#fff" stroke-width="2"/><path d="M5 12 l5 6 L22 2" fill="none" stroke="#fff" stroke-width="2.6"/></svg>Virus Protection</li>
        <li class="plan-item"><svg class="tick" viewBox="0 0 24 24"><rect x="1.5" y="3.5" width="19" height="19" fill="none" stroke="#fff" stroke-width="2"/><path d="M5 12 l5 6 L22 2" fill="none" stroke="#fff" stroke-width="2.6"/></svg>Data Backups</li>
        <li class="plan-item"><svg class="tick" viewBox="0 0 24 24"><rect x="1.5" y="3.5" width="19" height="19" fill="none" stroke="#fff" stroke-width="2"/><path d="M5 12 l5 6 L22 2" fill="none" stroke="#fff" stroke-width="2.6"/></svg>System Updates</li>
        <li class="plan-item"><svg class="tick" viewBox="0 0 24 24"><rect x="1.5" y="3.5" width="19" height="19" fill="none" stroke="#fff" stroke-width="2"/><path d="M5 12 l5 6 L22 2" fill="none" stroke="#fff" stroke-width="2.6"/></svg>Unlimited Support</li>
      </ul>
      <p class="plan-price">Just $19.95 a month!</p>
    </section>

    <div class="contact">
      <span class="contact-phone">(555)-310-2798</span>
      <span class="contact-web">www.qadtechhelp.net</span>
    </div>
  </main>
</body>
</html>
```